Business Card Design Project

We are looking for an eye catching, unique business card design that incorporates our logo and a photo of the mortgage associate.

We will need to have our business address included (could be on the back of the card), as well as the mortgage associate's information:

Name
Position
Phone
Email

Logo attached.

Target Market(s)

Clients (people purchasing homes, renewing existing mortgages, or refinancing existing mortgages)
Referral sources such as realtors, financial advisors, relocation specialists, real estate lawyers...

Industry/Entity Type

Business

Requirements
Must have
• Logo
Name and contact information of associate
Address of brokerage
Nice to have
• Photo of the agent

```html
<!DOCTYPE html>
<html lang="en">
<head>
<meta charset="utf-8">
<title>Keystone Lending Group – Business Card</title>
<link rel="stylesheet" href="https://fonts.googleapis.com/css2?family=Open+Sans:wght@400;600;700;800&display=swap">
<style>
  :root {
    --brand-red: #85161a;
    --card-white: #f1f1f1;
    --ink: #1b1b1b;
    --photo-grey: #9b9b9b;
    --accent-blue: #5a6d93;
    --backdrop: #d9d9d9;
  }
  * { margin: 0; padding: 0; box-sizing: border-box; }
  html, body {
    width: 1200px;
    height: 1200px;
    overflow: hidden;
    background: var(--backdrop);
    font-family: "Open Sans", Arial, sans-serif;
  }
  .canvas {
    position: relative;
    width: 1200px;
    height: 1200px;
  }
  .card {
    position: absolute;
    left: 150px;
    width: 900px;
    height: 514px;
    box-shadow: 0 10px 28px rgba(0,0,0,0.18);
  }
  .card--front { top: 52px; }
  .card--back { top: 634px; }
  .card svg { display: block; width: 900px; height: 514px; }
  .brand-name {
    font-family: "Open Sans", Arial, sans-serif;
    font-weight: 800;
    fill: var(--ink);
    letter-spacing: 0.5px;
  }
  .associate-name { font-weight: 700; font-size: 30px; fill: #fff; }
  .associate-detail { font-weight: 400; font-size: 28px; fill: #fff; }
  .address-text { font-weight: 400; font-size: 25px; fill: #fff; }
</style>
</head>
<body>
<main class="canvas">

  <!-- Front face -->
  <section class="card card--front" aria-label="Business card front">
    <svg viewBox="0 0 900 514" xmlns="http://www.w3.org/2000/svg">
      <rect class="card-base" width="900" height="514" fill="var(--card-white)"/>
      <path class="swoop-accent" d="M0,278 C310,250 640,120 900,-8 L900,6 C640,134 310,264 0,292 Z" fill="var(--accent-blue)"/>
      <path class="swoop-band" d="M0,290 C310,262 640,132 900,4 L900,514 L0,514 Z" fill="var(--brand-red)"/>

      <rect class="associate-photo" role="img" aria-label="Photo of the mortgage associate" x="620" y="34" width="170" height="190" rx="14" fill="var(--photo-grey)"/>

      <g class="brand-lockup">
        <rect x="52" y="92" width="30" height="30" fill="var(--brand-red)"/>
        <text class="brand-name" x="96" y="106" font-size="30">KEYSTONE</text>
        <text class="brand-name" x="96" y="136" font-size="30">LENDING GROUP</text>
      </g>

      <g class="associate-info">
        <text class="associate-name" x="60" y="368">Mr. Daniel Mensah</text>
        <text class="associate-detail" x="60" y="406">President</text>
        <text class="associate-detail" x="60" y="444">555-555-555</text>
        <text class="associate-detail" x="60" y="482">email@email.com</text>
      </g>
    </svg>
  </section>

  <!-- Back face -->
  <section class="card card--back" aria-label="Business card back">
    <svg viewBox="0 0 900 514" xmlns="http://www.w3.org/2000/svg">
      <rect class="card-base" width="900" height="514" fill="var(--card-white)"/>
      <rect class="top-band" width="900" height="250" fill="var(--brand-red)"/>
      <polygon class="house-notch" points="250,251 250,160 330,112 660,112 660,251" fill="var(--card-white)"/>

      <g class="brand-lockup">
        <rect x="276" y="170" width="30" height="30" fill="var(--brand-red)"/>
        <text class="brand-name" x="320" y="186" font-size="32">KEYSTONE</text>
        <text class="brand-name" x="320" y="218" font-size="32">LENDING GROUP</text>
      </g>

      <g class="address-block">
        <rect x="300" y="268" width="230" height="190" fill="var(--brand-red)"/>
        <text class="address-text" x="318" y="310">Company's</text>
        <text class="address-text" x="318" y="346">Address And</text>
        <text class="address-text" x="318" y="382">Number Goes</text>
        <text class="address-text" x="318" y="418">Here.</text>
      </g>
    </svg>
  </section>

</main>
</body>
</html>
```